need professional, precise design for a website

I will start with a homepage design and if we pick your design, we'll have you design up to 6 more interior pages (we'll pay extra for these of course). We need a homepage design for a reserve study company based in Idaho, covering the northwest region. The company is called copper ridge reserve study. Their current site is at https://www.copperridgereserves.example/ and they really like this site for inspiration https://www.fundplannerhub.example/ but they would like an original design, just more modern and fresh like the sample site. I have logo files I will attach. They want something that looks financial and has a feel of accuity. Their main call to action will be to have someone fill in a contact form or call them on the phone. They will have a sample study that someone can download as on the fundplannerhub site. You can use copy from their current site.

```html
<!DOCTYPE html>
<html lang="en">
<head>
<meta charset="utf-8">
<title>Copper Ridge Reserves — Reserve Studies for the Northwest</title>
<link href="https://fonts.googleapis.com/css2?family=Raleway:wght@400;500;600;700;800&display=swap" rel="stylesheet">
<style>
:root{
  --teal:#27a6d2;
  --teal-dark:#1d87ad;
  --green:#6aab1f;
  --green-dark:#5a9418;
  --navy:#1b2a45;
  --ink:#2b2b2b;
  --body:#5d6268;
  --muted:#9aa0a6;
  --paper:#ffffff;
  --mist:#eeeeef;
  --line:#d9dde1;
}
*{box-sizing:border-box;margin:0;padding:0}
html,body{width:1200px;height:4215px;overflow:hidden}
body{font-family:"Raleway",Arial,sans-serif;color:var(--body);background:var(--mist)}
section,header,footer{position:relative;width:1200px;overflow:hidden}
.abs{position:absolute}
.btn{position:absolute;display:flex;align-items:center;justify-content:center;color:#fff;font-size:13px;font-weight:600;border:1px solid rgba(255,255,255,.6)}
.btn-teal{background:var(--teal)}
.btn-green{background:var(--green)}
.card{position:absolute;background:var(--paper);box-shadow:0 4px 18px rgba(0,0,0,.12)}
.tab{position:absolute;height:52px;display:flex;align-items:center}
.tab svg{position:absolute;top:0;left:0}
.tab span{position:relative;font-size:25px;font-weight:700;color:var(--ink);white-space:nowrap}
.photo{position:absolute}

/* nav */
.site-nav{height:50px;background:#fff}
.brand{position:absolute;left:232px;top:14px;display:flex;align-items:center;gap:8px;font-size:15px;font-weight:600;color:var(--navy)}
.brand i{display:block;width:14px;height:14px;border-radius:50%;background:var(--navy)}
.menu{position:absolute;left:505px;top:17px;display:flex;gap:38px;font-size:12px;color:#555}
.menu .active{color:var(--teal);border-bottom:2px solid var(--teal);padding-bottom:4px}

/* hero */
.hero{height:405px}
.hero-title{position:absolute;left:330px;top:96px;width:547px;height:135px;background:rgba(40,45,110,.72);border:6px solid rgba(255,255,255,.18);display:flex;align-items:center;justify-content:center;text-align:center;color:#fff;font-size:29px;font-weight:700;line-height:1.35}

/* about */
.about{height:458px;background:var(--mist)}
.about p{position:absolute;left:14px;width:350px;font-size:12.5px;line-height:20px;color:var(--body)}
.play{position:absolute;left:50%;top:50%;transform:translate(-50%,-50%)}

/* banner */
.banner{height:157px}
.banner h2{position:absolute;top:38px;width:100%;text-align:center;color:#fff;font-size:23px;font-weight:700}
.banner .or{position:absolute;left:572px;top:84px;width:56px;height:34px;display:flex;align-items:center;justify-content:center;color:#fff;font-weight:800;font-size:18px}

/* services */
.services{height:582px;background:var(--mist)}
.svc-frame{position:absolute;left:8px;top:84px;width:582px;height:357px;border:2px solid var(--teal)}
.frame-brand{position:absolute;top:14px;left:0;width:100%;display:flex;align-items:center;justify-content:center;gap:10px}
.frame-brand b{font-size:22px;font-weight:600;color:var(--navy)}
.frame-brand i{display:block;width:20px;height:20px;border-radius:50%;background:var(--navy)}
.frame-brand hr{flex:1;border:0;border-top:2px solid var(--teal);margin:0 14px}
.svc{position:absolute;top:104px;width:160px;height:186px;border:1px solid var(--line);background:#fff;text-align:center;padding:10px 12px}
.svc.feature{border-color:var(--green)}
.svc h3{font-size:12px;font-weight:600;color:var(--teal);line-height:16px;margin:6px 0 8px;min-height:32px}
.svc p{font-size:10px;line-height:14px;color:var(--muted)}
.svc .more{position:absolute;left:0;bottom:0;width:100%;height:22px;font-size:10px;color:var(--ink);border-bottom:3px solid var(--teal-dark);display:flex;align-items:center;justify-content:center;gap:6px}
.svc.feature .more{border-bottom-color:var(--green)}

/* reserve studies */
.studies{height:568px}
.studies-panel{position:absolute;left:225px;top:54px;width:750px;height:464px;background:rgba(20,24,28,.62)}
.studies h3{position:absolute;left:388px;top:84px;color:#fff;font-size:22px;font-weight:700}
.studies .copy{position:absolute;left:388px;top:126px;width:345px;color:#e9ecef;font-size:11.5px;line-height:17px}
.studies .copy p{margin-bottom:10px}
.studies .copy li{list-style:none;position:relative;padding-left:14px;margin-bottom:8px}
.studies .copy li::before{content:"";position:absolute;left:0;top:5px;width:8px;height:8px;background:#fff}

/* blog */
.blog{height:604px;background:var(--mist)}
.spark{position:absolute;left:8px;top:112px;width:354px;height:169px;background:var(--green)}
.spark-inner{position:absolute;inset:10px;border:2px solid rgba(255,255,255,.85)}
.spark .name{position:absolute;left:18px;top:22px;display:flex;align-items:center;gap:8px;color:#fff;font-size:20px;font-weight:600}
.spark .name i{display:block;width:18px;height:18px;border-radius:50%;background:#fff}
.spark .lead{position:absolute;left:18px;top:92px;color:#fff;font-size:14px;font-weight:700}
.spark .go{position:absolute;right:18px;bottom:16px;width:112px;height:28px;background:#fff;color:var(--green);font-size:12px;display:flex;align-items:center;justify-content:center}
.post{position:absolute;width:169px;height:169px}
.post .title{position:absolute;left:8px;bottom:28px;width:150px;color:#fff;font-size:12.5px;font-weight:700;line-height:16px;text-shadow:0 1px 3px rgba(0,0,0,.5)}
.post .go{position:absolute;right:10px;bottom:8px;color:var(--green);font-size:10.5px;font-weight:600}

/* subscribe */
.subscribe{height:169px;background:#e6e6e7}
.subscribe h2{position:absolute;top:26px;width:100%;text-align:center;font-size:25px;font-weight:700;color:var(--ink)}
.subscribe h2 em,.testimonial h2 em{font-style:normal;color:var(--green)}
.sub-input{position:absolute;left:365px;top:98px;width:360px;height:35px;background:#fff;font-size:11px;color:var(--muted);padding:11px 12px}
.sub-btn{position:absolute;left:725px;top:98px;width:110px;height:35px;background:var(--green);color:#fff;font-size:12px;display:flex;align-items:center;justify-content:center}

/* testimonial */
.testimonial{height:379px;background:#fff;text-align:center}
.testimonial h2{position:absolute;top:48px;width:100%;font-size:25px;font-weight:700;color:var(--ink)}
.avatar{position:absolute;left:574px;top:97px;width:52px;height:52px;border-radius:50%;background:linear-gradient(160deg,#b9bcc0,#6f747a)}
.who{position:absolute;top:164px;width:100%;font-size:13px;color:var(--ink)}
.quote{position:absolute;left:365px;top:192px;width:470px;font-size:11.5px;line-height:19px;color:var(--body)}
.qmark{position:absolute;font-family:Georgia,serif;font-size:170px;line-height:1;color:#e4e4e4}

/* contact */
.contact{height:534px;background:linear-gradient(160deg,#27436a,#17284a 55%,#0f1c36)}
.form{position:absolute;left:599px;top:42px;width:376px;height:472px;background:#fff}
.field{position:absolute;width:160px}
.field label{display:block;font-size:9.5px;color:var(--teal);margin-bottom:3px}
.field div{height:20px;border:1px solid var(--line);font-size:8.5px;color:var(--muted);padding:4px 6px;white-space:nowrap;overflow:hidden}
.check{position:absolute;font-size:8.5px;color:var(--muted);display:flex;align-items:center;gap:4px}
.check i{display:block;width:8px;height:8px;border:1px solid var(--muted)}

/* footer */
.site-footer{height:309px;background:#fff;text-align:center}
.foot-brand{position:absolute;top:40px;width:100%;display:flex;align-items:center;justify-content:center;gap:12px;font-size:36px;font-weight:600;color:var(--navy)}
.foot-brand i{display:block;width:30px;height:30px;border-radius:50%;background:var(--navy)}
.foot-info{position:absolute;top:146px;width:100%;font-size:12px;line-height:18px;color:#555}
.copyright{position:absolute;top:287px;width:100%;font-size:11px;color:#555}
</style>
</head>
<body>

<header class="site-nav">
  <div class="brand"><i></i>Copper Ridge Reserves</div>
  <nav class="menu">
    <span class="active">Home</span><span>About Us</span><span>Our Services</span><span>Reserve Studies</span><span>Blog</span><span>Contact Us</span>
  </nav>
</header>

<section class="hero">
  <div class="photo" role="img" aria-label="Lakeside home with a stone terrace and dock at dusk" style="inset:0;background:linear-gradient(180deg,#7f9fbe 0%,#5c7d9f 38%,#3d5a76 62%,#8aa3b3 100%)"></div>
  <h1 class="hero-title">Rely on the Experts to Budget<br>Responsibly with a Reserve Study</h1>
  <div class="btn btn-teal" style="left:553px;top:287px;width:110px;height:31px">Contact Us</div>
</section>

<section class="about">
  <div class="card" style="left:225px;top:50px;width:750px;height:372px">
    <div class="tab" style="left:0;top:0;width:270px">
      <svg width="270" height="52" aria-hidden="true"><polygon points="0,0 48,0 0,52" fill="#6aab1f"/><polygon points="222,0 270,0 270,52" fill="#27a6d2"/></svg>
      <span style="left:64px">About Us</span>
    </div>
    <p style="top:84px">A reserve study is a clear plan for the future of your community. Knowing the right points of origin and following a steady map helps boards stay ahead of costly repairs and surprise assessments.</p>
    <p style="top:172px">We have spent years guiding associations through budgets, inspections and long range planning. Every plan we deliver is built to be precise, practical and easy for owners to follow.</p>
    <div class="btn btn-green" style="left:14px;top:287px;width:126px;height:31px">Read More</div>
    <svg class="abs" style="left:385px;top:62px" width="362" height="282" aria-hidden="true"><polygon points="362,0 362,40 322,0" fill="#27a6d2"/><polygon points="0,282 0,242 40,282" fill="#27a6d2"/></svg>
    <div class="photo" role="img" aria-label="Two-storey suburban home at twilight, video preview" style="left:393px;top:65px;width:346px;height:265px;background:linear-gradient(180deg,#3c5f93 0%,#5a78a8 45%,#4d5a4a 80%,#3f4a3a 100%)">
      <svg class="play" width="52" height="52" aria-hidden="true"><circle cx="26" cy="26" r="25" fill="#fff"/><polygon points="21,15 37,26 21,37" fill="#27a6d2"/></svg>
    </div>
  </div>
</section>

<section class="banner">
  <div class="photo" role="img" aria-label="Aerial view of a tropical island shoreline" style="inset:0;background:linear-gradient(180deg,#23486a 0%,#1c6c87 45%,#2e8c93 60%,#1c3f5a 100%)"></div>
  <h2>Your Financial Road Map For The Next 30 Years!</h2>
  <div class="btn btn-green" style="left:412px;top:84px;width:160px;height:34px">Call (208) 555-0148</div>
  <span class="or">OR</span>
  <div class="btn btn-green" style="left:628px;top:84px;width:158px;height:34px">Request A Quote</div>
</section>

<section class="services">
  <div class="card" style="left:225px;top:40px;width:750px;height:525px">
    <div class="tab" style="left:463px;top:0;width:287px">
      <svg width="287" height="52" aria-hidden="true"><polygon points="0,52 40,0 40,52" fill="#6aab1f"/><polygon points="239,0 287,0 287,52" fill="#27a6d2"/></svg>
      <span style="left:58px">Our Services</span>
    </div>
    <div class="svc-frame">
      <div class="frame-brand"><hr><i></i><b>Copper Ridge Reserves</b><hr></div>
      <div class="svc" style="left:17px">
        <svg width="24" height="22" aria-hidden="true"><rect x="3" y="6" width="18" height="14" fill="none" stroke="#1d87ad" stroke-width="2"/><path d="M7 10h3M14 10h3M7 15h3M14 15h3M1 6h22" stroke="#1d87ad" stroke-width="2"/></svg>
        <h3>Association Governed Communities</h3>
        <p>Long range funding plans for HOAs and condo boards, built on careful site visits and clear numbers.</p>
        <div class="more">Read More <span>→</span></div>
      </div>
      <div class="svc feature" style="left:206px">
        <svg width="24" height="22" aria-hidden="true"><path d="M2 11 12 3l10 8M5 9v11h14V9" fill="none" stroke="#6aab1f" stroke-width="2"/></svg>
        <h3>Vacation Ownership Reports</h3>
        <p>Reserve reports for resorts and timeshare groups that keep shared amenities funded year after year.</p>
        <div class="more">Read More <span>→</span></div>
      </div>
      <div class="svc" style="left:395px">
        <svg width="24" height="22" aria-hidden="true"><path d="M2 8 12 2l10 6H2zM4 19h16M6 10v8M10 10v8M14 10v8M18 10v8" fill="none" stroke="#1d87ad" stroke-width="2"/></svg>
        <h3>Municipalities &amp; Commercial Properties</h3>
        <p>Capital planning for city buildings, public facilities and commercial sites of every size and type.</p>
        <div class="more">Read More <span>→</span></div>
      </div>
      <svg class="abs" style="left:262px;top:312px" width="58" height="24" aria-hidden="true"><path d="M2 7h22M2 7l6-5M2 7l6 5" stroke="#333" stroke-width="2" fill="none"/><path d="M56 17H34M56 17l-6-5M56 17l-6 5" stroke="#333" stroke-width="2" fill="none"/></svg>
    </div>
    <div class="photo" role="img" aria-label="Smiling consultant in a white blouse" style="left:576px;top:148px;width:169px;height:293px;background:linear-gradient(180deg,#f4f4f4 0%,#e5e5e7 60%,#d8d9dc 100%)"></div>
    <div class="btn btn-teal" style="left:239px;top:475px;width:126px;height:31px">Read More</div>
  </div>
</section>

<section class="studies">
  <div class="photo" role="img" aria-label="Resort courtyard with palm trees" style="inset:0;background:linear-gradient(180deg,#5b6a63 0%,#3f4d44 45%,#6f7a73 75%,#8c9491 100%)"></div>
  <div class="studies-panel">
    <div class="tab" style="left:433px;top:0;width:317px">
      <svg width="317" height="52" aria-hidden="true"><polygon points="0,52 40,0 40,52" fill="#6aab1f"/><rect x="40" y="0" width="229" height="52" fill="#fff"/><polygon points="269,0 317,0 317,52" fill="#27a6d2"/></svg>
      <span style="left:54px">Reserve Studies</span>
    </div>
    <div class="photo" role="img" aria-label="Community pool beside a clubhouse under a blue sky" style="left:17px;top:87px;width:343px;height:272px;background:linear-gradient(180deg,#5d95d6 0%,#a7c7ea 40%,#e7e7de 62%,#4ab3c9 100%)"></div>
    <h3>What is a Reserve Study?</h3>
    <div class="copy">
      <p>At its core, a reserve study is a financial projection of income and expenses over a set period of time. Dozens of factors shape it, and each one has a lasting effect on those expenses.</p>
      <p>Here is a brief list of key items that make up a reserve study and how they affect your association:</p>
      <ul>
        <li>A physical inspection, review and analysis of all community assets the association is required to maintain, repair or replace.</li>
        <li>A complete list of maintenance and replacement items with a schedule over thirty years and the expected life of every component.</li>
      </ul>
    </div>
    <div class="btn btn-green" style="left:315px;top:390px;width:123px;height:31px">Read More</div>
  </div>
</section>

<section class="blog">
  <div class="card" style="left:225px;top:42px;width:750px;height:506px">
    <div class="tab" style="left:0;top:0;width:270px">
      <svg width="270" height="52" aria-hidden="true"><polygon points="0,0 48,0 0,52" fill="#6aab1f"/><polygon points="222,0 270,0 270,52" fill="#27a6d2"/></svg>
      <span style="left:64px">Our Blog</span>
    </div>
    <div class="spark">
      <div class="spark-inner"></div>
      <div class="name"><i></i>Copper Ridge Reserves</div>
      <div class="lead">Just A Spark Of Our Blog</div>
      <div class="go">Read More</div>
    </div>
    <div class="post" role="img" aria-label="Tropical resort at sunset" style="left:385px;top:112px;background:linear-gradient(180deg,#3a5f8c,#2f4f5c 60%,#1d2b2c)"><div class="title">HOA &amp; Condominium Studies</div><div class="go">Read More →</div></div>
    <div class="post" role="img" aria-label="Resort pool with palm trees" style="left:573px;top:112px;background:linear-gradient(180deg,#4d86c4,#6aa3a8 55%,#2e5a55)"><div class="title">Why Reserve Plans Matter</div><div class="go">Read More →</div></div>
    <div class="post" role="img" aria-label="Modern apartment building at dusk" style="left:8px;top:301px;background:linear-gradient(180deg,#4c6c96,#3d4e64 60%,#25303c)"><div class="title">Real Estate Gains of Strong Reserves</div><div class="go">Read More →</div></div>
    <div class="post" role="img" aria-label="White condominium facade" style="left:196px;top:301px;background:linear-gradient(180deg,#8eb2d8,#c9d3dc 55%,#7f8c97)"><div class="title">Skimping on Reserve Contributions</div><div class="go">Read More →</div></div>
    <div class="post" role="img" aria-label="Residential towers against a blue sky" style="left:385px;top:301px;background:linear-gradient(180deg,#2b5ea0,#4f77a3 55%,#38475a)"><div class="title">How to Fund Common Area Repairs?</div><div class="go">Read More →</div></div>
    <div class="post" role="img" aria-label="Lit pool and cabanas at night" style="left:573px;top:301px;background:linear-gradient(180deg,#1f3356,#2d5a7c 55%,#1b2638)"><div class="title">HOA &amp; Condominium Studies</div><div class="go">Read More →</div></div>
  </div>
</section>

<section class="subscribe">
  <svg class="abs" style="left:0;top:0" width="1200" height="169" aria-hidden="true"><polygon points="0,169 240,0 380,0 120,169" fill="#f1f1f2"/><polygon points="820,169 1060,0 1200,0 1200,60 1040,169" fill="#f1f1f2"/><polygon points="1020,169 1200,80 1200,169" fill="#dcdcde"/></svg>
  <h2>Subscribe Our <em>Newsletter</em></h2>
  <div class="sub-input">Enter Your Email Address</div>
  <div class="sub-btn">Subscribe</div>
</section>

<section class="testimonial">
  <h2>Our <em>Testimonial</em></h2>
  <div class="avatar" role="img" aria-label="Client portrait"></div>
  <div class="who">Dana &amp; Mel Hart</div>
  <span class="qmark" style="left:250px;top:185px">“</span>
  <span class="qmark" style="left:865px;top:185px">”</span>
  <p class="quote">Our board finally has a plan we can trust. The team walked every part of our property, explained each line of the report and gave us a funding schedule that owners understood right away. Meetings are calmer, budgets are steady and we no longer fear the next big repair. We recommend them to every association we know.</p>
  <svg class="abs" style="left:571px;top:320px" width="58" height="24" aria-hidden="true"><path d="M2 7h22M2 7l6-5M2 7l6 5" stroke="#333" stroke-width="2" fill="none"/><path d="M56 17H34M56 17l-6-5M56 17l-6 5" stroke="#333" stroke-width="2" fill="none"/></svg>
</section>

<section class="contact">
  <div class="photo" role="img" aria-label="Street map of the office location with a pin" style="left:225px;top:42px;width:374px;height:472px;background:linear-gradient(160deg,#c9d4da,#dfe4e2 50%,#b9c9d3)"></div>
  <div class="form">
    <div class="tab" style="left:89px;top:0;width:287px">
      <svg width="287" height="52" aria-hidden="true"><polygon points="0,52 40,0 40,52" fill="#6aab1f"/><polygon points="239,0 287,0 287,52" fill="#27a6d2"/></svg>
      <span style="left:58px">Contact Us</span>
    </div>
    <div class="field" style="left:14px;top:99px"><label>Name*</label><div>Enter Name</div></div>
    <div class="field" style="left:202px;top:99px"><label>Surname*</label><div>Enter Surname</div></div>
    <div class="field" style="left:14px;top:155px"><label>Email*</label><div>Enter Email Address</div></div>
    <div class="field" style="left:202px;top:155px"><label>Phone Number</label><div>Enter Phone Number</div></div>
    <div class="check" style="left:14px;top:194px"><i></i>Send me a text reply</div>
    <div class="field" style="left:14px;top:211px"><label>Preferred Contact Method</label><div>Select Email or Phone</div></div>
    <div class="field" style="left:202px;top:211px"><label>Name Of Property</label><div>Enter Name Of Property</div></div>
    <div class="field" style="left:14px;top:267px"><label>Address*</label><div>Enter Your Address</div></div>
    <div class="field" style="left:202px;top:267px"><label>Choose Type Of Reserve*</label><div>HOA Homeowners Association</div></div>
    <div class="field" style="left:14px;top:323px;width:348px"><label>Questions</label><div style="height:62px">Enter comments and details here</div></div>
    <div class="btn btn-teal" style="left:126px;top:416px;width:112px;height:28px">Read More</div>
  </div>
</section>

<footer class="site-footer">
  <div class="foot-brand"><i></i>Copper Ridge Reserves</div>
  <div class="foot-info">
    Copper Ridge Reserves, LLC<br>
    Serving Idaho, Montana, Oregon,<br>
    Utah, Washington &amp; Wyoming<br>
    Phone: (208) 555-0148<br>
    E-mail: info@copperridgereserves.example
  </div>
  <div class="copyright">Copyright Copper Ridge Reserves, LLC © 2019 All Rights Reserved</div>
</footer>

</body>
</html>
```